Amazing Sexy Elegant Eyecatching Wine Label

We need a label designed for our wine which is going to be produced very soon.

Needs to be on a grey scale, as colours increase the price per label dramatically.

Needs to have the "Crown" logo (file attached) included on the front and back label. Logo can be in black/white but can not be changed in any way, circle around the crown must stay there as well.

We are still unsure of whether to use "Harrowby Wine" or "Harrowby" as the brand for the label, if you could submit designs based around the two names we would appreciate that.

We will have 5 varieties, including; Sauvignon Blanc, Chardonnay, Pinot Gris, Riesling and Pinot Noir. So text needs to be easily changed.

We are after an image on the label which is modern and eye catching, even in a grey scale.

Please see other attached files for an idea we have done previously, we want something a bit more "designer" though. Some information on the label is a legal requirement and needs to be kept.

Target Market(s)

Wine Consumers

Requirements
Must have
• Crown Logo, Harrowby/Harrowby Wine brand, Grey Scale, Modern Design

```html
<!DOCTYPE html>
<html lang="en">
<head>
<meta charset="utf-8">
<title>Harrowby Wine – Sauvignon Blanc Label</title>
<link rel="stylesheet" href="https://fonts.googleapis.com/css2?family=Crimson+Text:wght@400&family=Yellowtail&family=Montserrat:wght@600&display=swap">
<style>
  :root {
    --page: #f2eee7;
    --label: #141414;
    --label-edge: #2a2a2a;
    --ink: #f4f4f2;
    --ink-soft: #a9a9a6;
    --ink-faint: #4a4a48;
    --ornament: #8d8d8a;
  }
  * { margin: 0; padding: 0; box-sizing: border-box; }
  html, body {
    width: 960px; height: 1200px; overflow: hidden;
    background: var(--page);
  }
  .canvas {
    position: relative; width: 960px; height: 1200px;
  }
  .label {
    position: absolute; left: 280px; top: 85px;
    width: 400px; height: 1030px;
    background: var(--label);
    border: 2px solid var(--label-edge);
    box-shadow: inset 0 0 0 10px var(--label), inset 0 0 0 11px #232323;
    color: var(--ink);
    font-family: "Crimson Text", Georgia, serif;
    text-align: center;
  }
  .brand-seal {
    position: absolute; left: 146px; top: 165px;
    width: 108px; height: 108px;
    border: 3px solid var(--ink); border-radius: 50%;
    display: flex; align-items: center; justify-content: center;
    font-size: 16px; line-height: 1.1; letter-spacing: 1px;
    color: var(--ink);
  }
  .brand-name {
    position: absolute; left: 0; right: 0; top: 318px;
    font-family: "Yellowtail", cursive;
    font-size: 60px; line-height: 1; color: var(--ink);
  }
  .brand-sub {
    position: absolute; left: 0; right: 0; top: 402px;
    font-size: 18px; color: var(--ink);
  }
  .flourish-block {
    position: absolute; left: 30px; top: 450px; width: 340px; height: 186px;
  }
  .flourish-art {
    position: absolute; left: 110px; top: 30px; width: 120px; height: 126px;
    background: radial-gradient(ellipse at center, #6e6e6b 0%, #3a3a38 55%, var(--label) 80%);
  }
  .variety {
    position: absolute; left: 0; right: 0; top: 660px;
    font-size: 33px; color: var(--ink);
  }
  .tagline {
    position: absolute; left: 0; right: 0; top: 722px;
    font-size: 14px; color: var(--ink-soft);
  }
  .brand-line {
    position: absolute; left: 0; right: 0; top: 792px;
    font-size: 14px; color: var(--ink-soft); letter-spacing: 1px;
  }
  .abv {
    position: absolute; left: 22px; top: 940px;
    font-family: "Montserrat", Arial, sans-serif; font-weight: 600;
    font-size: 28px; color: var(--ink);
  }
  .abv small { font-size: 10px; font-weight: 600; }
  .volume {
    position: absolute; right: 24px; top: 940px;
    font-size: 32px; color: var(--ink-faint);
  }
  .volume small { font-size: 12px; }
</style>
</head>
<body>
<main class="canvas">
  <section class="label">
    <div class="brand-seal">Harrowby<br>Wine</div>
    <h1 class="brand-name">Harrowby</h1>
    <p class="brand-sub">Wine</p>

    <div class="flourish-block">
      <svg width="340" height="186" viewBox="0 0 340 186">
        <g stroke="var(--ornament)" stroke-width="1.2" fill="none">
          <line x1="0" y1="70" x2="130" y2="70"/>
          <line x1="210" y1="70" x2="340" y2="70"/>
          <line x1="20" y1="116" x2="130" y2="116"/>
          <line x1="210" y1="116" x2="320" y2="116"/>
        </g>
        <g fill="var(--ink)">
          <path d="M170 0 L176 9 L170 18 L164 9 Z"/>
          <path d="M170 168 L176 177 L170 186 L164 177 Z"/>
        </g>
      </svg>
      <div class="flourish-art" role="img" aria-label="Symmetrical ornamental flourish with swirling leaves"></div>
    </div>

    <h2 class="variety">Sauvignon Blanc</h2>
    <p class="tagline">Delightfully refreshing</p>
    <p class="brand-line">Harrowby Wine</p>

    <p class="abv">11%<small>VOL.</small></p>
    <p class="volume">750<small>ml</small></p>
  </section>
</main>
</body>
</html>
```